Design business card for new business which advocates for elders in nursing homes or personal care h

New business for rights of the elderly residents who reside in personal care homes and or nursing homes. I am looking for a business card with logo of keystone for Pennsylvania and something in side the keystone that represents healthcare, advocates, something on that line; monitor care received and needs of resident. Chart audits, State Regulation compliance

Target Market(s)

Seniors no longer safe to live at home by themselves along with their kids

Industry/Entity Type

Business

Contact Information for Business Card

Keystone symbol to represent Pensylvaoa with some kind of symbol inside to represent advocate, seniors, or healthcare symbol

Font styles to use
Serif

Colors
33a6d7
85cae6
abd037

Requirements
Must have
• Brightwell Elder Allies is our business name; our tag line is Path to Better Living
Nice to have
• Nice logo

```html
<!DOCTYPE html>
<html lang="en">
<head>
<meta charset="utf-8">
<title>Brightwell Elder Allies – Business Card</title>
<link rel="stylesheet" href="https://fonts.googleapis.com/css2?family=Lora:wght@400;600;700&display=swap">
<style>
  :root {
    --backdrop: #2b2b2d;
    --lime: #b3d340;
    --sky: #33a6d7;
    --sky-light: #85cae6;
    --ink: #3a3d40;
    --ink-soft: #3f4f5c;
    --slate: #5b5c5e;
    --slate-dark: #4a4b4d;
    --band: rgba(255, 255, 255, 0.42);
    --band-dark: rgba(255, 255, 255, 0.16);
    --pale-text: #c9cacb;
  }
  * { margin: 0; padding: 0; box-sizing: border-box; }
  html, body {
    width: 1200px; height: 816px; overflow: hidden;
    background: var(--backdrop);
    font-family: "Lora", serif;
  }
  .sheet { position: relative; width: 1200px; height: 816px; }
  .card {
    position: absolute; top: 253px;
    width: 540px; height: 310px;
    overflow: hidden;
    border-radius: 2px;
  }
  .card--back {
    left: 40px;
    background: linear-gradient(160deg, var(--slate) 0%, var(--slate-dark) 100%);
  }
  .card--front { left: 620px; }

  .card__field { position: absolute; inset: 0; width: 100%; height: 100%; }

  .band { position: absolute; left: 0; right: 0; }
  .card--back .band {
    top: 112px; height: 52px; background: var(--band-dark);
    display: flex; align-items: center; padding-left: 30px;
  }
  .web-banner {
    color: var(--pale-text); font-size: 30px; font-weight: 400;
    letter-spacing: 1.5px; text-transform: uppercase; white-space: nowrap;
  }

  .brand {
    position: absolute; left: 34px; top: 34px;
    display: flex; align-items: flex-start; gap: 10px;
  }
  .brand__mark {
    width: 30px; height: 30px; background: var(--ink); flex: none; margin-top: 2px;
  }
  .brand__name {
    font-size: 19px; font-weight: 700; color: var(--ink);
    text-transform: uppercase; letter-spacing: 0.3px; line-height: 1;
    margin-top: 3px;
  }
  .brand__tagline {
    font-size: 13px; font-weight: 400; color: var(--ink);
    margin-top: 5px; letter-spacing: 0.2px;
  }

  .card--front .band {
    top: 128px; height: 56px; background: var(--band);
    display: flex; align-items: center; padding-left: 56px; gap: 8px;
  }
  .person__name {
    font-size: 22px; font-weight: 400; color: var(--ink);
    text-transform: uppercase; letter-spacing: 0.5px; white-space: nowrap;
  }
  .person__role {
    font-size: 9px; font-weight: 600; color: var(--ink);
    text-transform: uppercase; letter-spacing: 0.5px; margin-top: 6px; white-space: nowrap;
  }

  .contact {
    position: absolute; right: 34px; bottom: 30px;
    list-style: none; text-align: right;
    color: var(--ink-soft); font-size: 12px; line-height: 1.4;
    text-transform: uppercase; letter-spacing: 0.4px;
  }
</style>
</head>
<body>
<main class="sheet">

  <section class="card card--back" aria-label="Card back">
    <div class="band">
      <span class="web-banner">www.brightwellea.org</span>
    </div>
  </section>

  <section class="card card--front" aria-label="Card front">
    <svg class="card__field" viewBox="0 0 540 310" preserveAspectRatio="none" aria-hidden="true">
      <rect width="540" height="310" fill="var(--sky)"/>
      <polygon points="0,0 470,0 0,230" fill="var(--lime)"/>
      <polygon points="470,0 540,0 540,40 0,310 0,230" fill="var(--sky-light)" opacity="0.35"/>
    </svg>

    <header class="brand">
      <span class="brand__mark"></span>
      <div>
        <p class="brand__name">Brightwell Elder Allies</p>
        <p class="brand__tagline">Path to Better Living</p>
      </div>
    </header>

    <div class="band person">
      <span class="person__name">Daniel Whitford</span>
      <span class="person__role">Legal Counsel</span>
    </div>

    <ul class="contact">
      <li>Office: 555-555-5555</li>
      <li>Fax: 555-444-4444</li>
      <li>Email: daniel@brightwellea.org</li>
      <li>Web: www.brightwellea.org</li>
    </ul>
  </section>

</main>
</body>
</html>
```